Nectarine Point of Sale Cards for Grocery Retail Markets

We are looking to update our Nectarine point of sale card and price card. The cards will need to be 7" x 11" with a .125 bleed - one sided. See attached for the old versions. We would like this to use photos that look like true Washington State Peaches. Here are the bullet points we would like to use: - New Crop!- Tree Ripened- Excellent FlavorNOTE: The price card just needs to have a space where a retailer can write in the sale price of the item. See attachment with the white box.

Target Market(s)

Retail market shoppers

Requirements
Must have
• Pictures of Nectarines Only

```html
<!DOCTYPE html>
<html lang="en">
<head>
<meta charset="utf-8">
<title>Nectarine Point of Sale Cards</title>
<link rel="stylesheet" href="https://fonts.googleapis.com/css2?family=Cinzel:wght@700&family=Montserrat:wght@700;800&family=Yellowtail&display=swap">
<style>
  :root {
    --page: #ececec;
    --frame: #f6a21c;
    --paper: #f4f4f2;
    --red: #cc2027;
    --green: #1b6b35;
    --gold: #f2a91e;
    --white: #ffffff;
  }
  * { box-sizing: border-box; margin: 0; padding: 0; }
  html, body { width: 953px; height: 1200px; overflow: hidden; }
  body {
    background: var(--page);
    font-family: "Montserrat", Arial, sans-serif;
    position: relative;
  }
  .card {
    position: absolute;
    left: 46px;
    width: 860px;
    height: 547px;
    background: var(--frame);
  }
  .card--price { top: 38px; }
  .card--promo { top: 615px; }
  .card__inner {
    position: absolute;
    inset: 16px;
    background: linear-gradient(135deg, #fafafa 0%, #ececea 55%, #f7f7f5 100%);
    overflow: hidden;
  }
  .card__photo {
    position: absolute;
    left: 0; top: 80px;
    width: 500px; height: 435px;
    background:
      radial-gradient(ellipse at 30% 45%, #f7c64e 0%, #f1a53a 30%, transparent 55%),
      radial-gradient(ellipse at 70% 40%, #d8262c 0%, #c01c22 40%, transparent 70%),
      linear-gradient(90deg, #fff6e6 0%, #ffffff 100%);
  }
  .card__banner {
    position: absolute;
    left: 0; top: 0;
    width: 560px; height: 100px;
  }
  .card__title {
    position: absolute;
    left: 16px; top: 22px;
    font-family: "Cinzel", Georgia, serif;
    font-weight: 700;
    font-size: 24px;
    letter-spacing: 0.5px;
    color: var(--white);
  }
  .brand {
    position: absolute;
    left: 555px; top: 22px;
    display: flex;
    align-items: center;
    gap: 10px;
  }
  .brand__dot {
    width: 52px; height: 52px;
    border-radius: 50%;
    background: #e0572c;
  }
  .brand__name {
    font-weight: 700;
    font-size: 16px;
    line-height: 18px;
    color: var(--green);
  }
  .slogan {
    position: absolute;
    left: 482px; top: 112px;
    width: 330px;
  }
  .slogan__lead {
    font-family: "Yellowtail", cursive;
    font-size: 54px;
    line-height: 56px;
    color: var(--green);
  }
  .slogan__lead em {
    font-style: normal;
    font-size: 32px;
    color: var(--gold);
  }
  .slogan__stroke {
    position: absolute;
    left: 10px; top: 78px;
    width: 260px; height: 30px;
    background: linear-gradient(90deg, rgba(242,169,30,0) 0%, var(--gold) 25%, var(--gold) 80%, rgba(242,169,30,0) 100%);
    opacity: 0.85;
  }
  .slogan__main {
    position: relative;
    font-family: "Yellowtail", cursive;
    font-size: 62px;
    line-height: 62px;
    color: var(--red);
    padding-left: 18px;
  }
  .benefits {
    position: absolute;
    left: 488px;
    list-style: none;
    font-weight: 800;
    color: var(--green);
  }
  .card--price .benefits { top: 268px; font-size: 26px; line-height: 33px; }
  .card--promo .benefits { top: 296px; font-size: 28px; line-height: 40px; }
  .benefits li::before { content: "•"; margin-right: 4px; }
  .card--promo .benefits li::before { color: var(--gold); margin-right: 8px; }
  .price-box {
    position: absolute;
    left: 510px; top: 378px;
    width: 300px; height: 124px;
    background: var(--white);
  }
</style>
</head>
<body>

<section class="card card--price">
  <div class="card__inner">
    <div class="card__photo" role="img" aria-label="Photo of a halved nectarine with its pit beside a whole red nectarine"></div>
    <svg class="card__banner" viewBox="0 0 560 100" aria-hidden="true">
      <polygon points="0,0 560,0 490,72 0,60" fill="var(--red)"/>
      <polygon points="0,60 490,72 470,94 420,80 0,66" fill="var(--green)"/>
      <polygon points="0,66 420,80 470,94 0,84" fill="#ffffff"/>
    </svg>
    <h1 class="card__title">WASHINGTON STATE NECTARINES</h1>
    <div class="brand">
      <span class="brand__dot"></span>
      <span class="brand__name">Evergreen Orchard<br>Council</span>
    </div>
    <div class="slogan">
      <div class="slogan__lead">Taste <em>the</em></div>
      <div class="slogan__stroke" role="img" aria-label="Gold brush stroke"></div>
      <div class="slogan__main">Difference!</div>
    </div>
    <ul class="benefits">
      <li>New Crop!</li>
      <li>Tree Ripened</li>
      <li>Excellent Flavor</li>
    </ul>
    <div class="price-box"></div>
  </div>
</section>

<section class="card card--promo">
  <div class="card__inner">
    <div class="card__photo" role="img" aria-label="Photo of a halved nectarine with its pit beside a whole red nectarine"></div>
    <svg class="card__banner" viewBox="0 0 560 100" aria-hidden="true">
      <polygon points="0,0 560,0 490,72 0,60" fill="var(--red)"/>
      <polygon points="0,60 490,72 470,94 420,80 0,66" fill="var(--green)"/>
      <polygon points="0,66 420,80 470,94 0,84" fill="#ffffff"/>
    </svg>
    <h1 class="card__title">WASHINGTON STATE NECTARINES</h1>
    <div class="brand">
      <span class="brand__dot"></span>
      <span class="brand__name">Evergreen Orchard<br>Council</span>
    </div>
    <div class="slogan">
      <div class="slogan__lead">Taste <em>the</em></div>
      <div class="slogan__stroke" role="img" aria-label="Gold brush stroke"></div>
      <div class="slogan__main">Difference!</div>
    </div>
    <ul class="benefits">
      <li>New Crop!</li>
      <li>Tree Ripened</li>
      <li>Excellent Flavor</li>
    </ul>
  </div>
</section>

</body>
</html>
```